Records Management Company Revamp

We are looking to revamp our web presence, and need a catchy design that helps us to get noticed! We would like the website to be in wordpress. the main requirements are a home page, a landing page template for SEO / PPC, and then a few other pages that can be reused throughout the website.

We are happy to supply content / video etc.
Updates

Low designer entries

Have guaranteed payment and hoping to receive more designs

Number of Pages Required

3 page

Other font styles liked:
• Find fonts listed in attached branding document

Requirements
Must have
• Home page as well as sub pages according to their colours. Need to use colours and fonts set out in branding guide. Attached are examples of home page and sub pages.
Nice to have
• We have uploaded some very basic ideas we have of how we wish the website to look, but looking to have it more professional and fit together. Please see uploaded items.

```html
<!DOCTYPE html>
<html lang="en">
<head>
<meta charset="utf-8">
<title>Vaultline Records – Home</title>
<link rel="stylesheet" href="https://fonts.googleapis.com/css2?family=Roboto+Condensed:wght@400;700&family=Open+Sans:wght@400;600;700&display=swap">
<style>
:root{
  --blue:#2a78bd;
  --blue-dark:#1d4f7d;
  --navy:#16324f;
  --red:#e1262d;
  --orange:#f1602b;
  --green:#8dc63f;
  --pink:#b9446e;
  --grey-bg:#f2f2f2;
  --text:#4a4a4a;
  --footer:#1e2227;
  --footer-bottom:#15181b;
  --white:#fff;
}
*{box-sizing:border-box;margin:0;padding:0}
html,body{width:1200px;height:4232px;overflow:hidden}
body{font-family:"Open Sans",Arial,sans-serif;color:var(--text);font-size:14px;background:var(--white)}
.heading{font-family:"Roboto Condensed",Arial,sans-serif;font-weight:700;text-transform:uppercase;letter-spacing:.5px}
section,header{position:relative;width:1200px;overflow:hidden}

/* top bar */
.topbar{height:36px;display:flex;align-items:center;justify-content:space-between;padding:0 160px;font-size:12px;color:#666;background:var(--white)}
.topbar .left span{margin-right:24px}
.topbar .right{display:flex;align-items:center;gap:10px}
.dot{width:16px;height:16px;border-radius:50%;background:var(--blue);display:inline-block}
.cart{width:18px;height:14px;border:2px solid var(--blue);border-radius:2px;position:relative}
.cart-badge{width:12px;height:12px;border-radius:50%;background:var(--red);position:absolute;top:-8px;right:-8px}

/* header */
.site-header{height:96px;background:var(--blue);display:flex;align-items:center;padding:0 160px;justify-content:space-between}
.logo{display:flex;align-items:center;gap:10px;color:var(--white);font-family:"Roboto Condensed",sans-serif;font-weight:700;font-size:24px}
.logo .mark{width:28px;height:28px;background:var(--white)}
.nav{display:flex;gap:26px;color:var(--white);font-size:14px;font-weight:600;align-items:center}
.phone-btn{background:var(--red);color:var(--white);padding:10px 18px;font-weight:700;border-radius:3px}

/* hero */
.hero{height:460px}
.hero-photo{position:absolute;inset:0;background:linear-gradient(90deg,#cfe1ec 0%,#e9e4dc 35%,#d9b98f 60%,#c99a66 100%)}
.hero-headline{position:absolute;left:160px;top:328px;width:420px}
.hero-headline h1{display:inline;background:var(--navy);color:var(--white);font-size:30px;line-height:1.35;padding:2px 8px;box-decoration-break:clone;-webkit-box-decoration-break:clone}
.hero-headline p{margin-top:10px;display:inline-block;background:var(--orange);color:var(--white);font-weight:700;font-size:15px;padding:4px 8px;line-height:1.4}
.quote-form{position:absolute;left:688px;top:20px;width:432px;height:356px;background:rgba(241,96,43,.92);padding:16px 18px}
.quote-form h2{color:var(--white);font-size:17px;line-height:1.3;margin-bottom:12px}
.field{height:32px;background:var(--white);margin-bottom:8px;font-size:12px;color:#888;padding:8px 10px;display:flex;justify-content:space-between}
.form-btns{display:flex;gap:12px;margin-top:6px}
.btn{display:inline-block;background:var(--red);color:var(--white);font-family:"Roboto Condensed",sans-serif;font-weight:700;text-transform:uppercase;font-size:14px;padding:10px 22px;border-radius:2px;text-align:center}
.form-btns .btn{flex:1}

/* offer */
.offer{height:488px;padding-top:64px}
.section-title{text-align:center;font-size:26px;color:#333}
.section-title.light{color:var(--white)}
.offer-cards{display:flex;gap:48px;justify-content:center;margin-top:50px}
.offer-card{width:240px;height:268px;position:relative;color:var(--white)}
.offer-card .img{position:absolute;inset:0}
.offer-card h3{position:absolute;top:96px;width:100%;text-align:center;font-size:24px}
.offer-card p{position:absolute;top:150px;left:16px;right:16px;text-align:center;font-size:12px;padding:6px;line-height:1.4}
.c1 .img{background:linear-gradient(135deg,#b8363d,#e0616a)}.c1 p{background:rgba(160,30,40,.85)}
.c2 .img{background:linear-gradient(135deg,#7d9a3c,#b8c77a)}.c2 p{background:rgba(100,130,40,.85)}
.c3 .img{background:linear-gradient(135deg,#c98543,#f0c48d)}.c3 p{background:rgba(200,120,50,.85)}
.c4 .img{background:linear-gradient(135deg,#4f8fc4,#a7cbe6)}.c4 p{background:rgba(40,110,170,.85)}

/* about */
.about{height:420px;background:var(--grey-bg)}
.about-text{position:absolute;left:168px;top:104px;width:392px}
.about-text h2{font-size:26px;color:#333;margin-bottom:10px}
.about-text .lead{font-weight:700;font-size:13px;margin-bottom:12px}
.about-text p{font-size:12px;line-height:1.6;margin-bottom:18px}
.about-photo{position:absolute;left:608px;top:104px;width:420px;height:304px;background:linear-gradient(135deg,#b7c9d6,#e8ddd0 55%,#9fb6c6)}

/* steps */
.steps{height:560px}
.steps .section-title{margin-top:136px}
.step-row{display:flex;justify-content:center;gap:60px;margin-top:130px}
.step{width:236px;text-align:center}
.step svg{display:block;margin:0 auto 14px}
.step h4{font-size:13px;font-weight:700;color:#333;margin-bottom:6px}
.step p{font-size:11px;line-height:1.5}

/* team */
.team{height:520px;background:var(--blue-dark)}
.team .bg-shape{position:absolute;inset:0}
.team .section-title{position:relative;margin-top:128px}
.team-row{position:relative;display:flex;justify-content:center;gap:64px;margin-top:40px}
.member{width:152px;text-align:center;color:var(--white)}
.member .avatar{width:152px;height:152px;border-radius:50%;border:5px solid var(--white);background:linear-gradient(160deg,#9aa8b4,#56677a)}
.member h5{margin-top:12px;font-size:13px}
.member .role{font-size:11px;opacity:.85}
.member .socials{display:flex;gap:5px;justify-content:center;margin:8px 0}
.member .socials i{width:14px;height:14px;background:var(--white);opacity:.8;display:block}
.member .mail{font-size:10px}

/* cta */
.cta-strip{height:100px;background:var(--orange);display:flex;align-items:center;justify-content:center;gap:24px;color:var(--white)}
.cta-strip h3{font-size:26px}
.cta-strip .btn.alt{background:var(--white);color:var(--orange)}
.cta-strip .btn{background:var(--blue);}
.cta-strip .btn.red{background:var(--red);color:var(--white)}

/* testimonial */
.testimonial{height:580px}
.testimonial .img{position:absolute;inset:0;background:linear-gradient(180deg,#1f4770,#173a5e 50%,#123050)}
.testimonial .inner{position:relative;text-align:center;color:var(--white);padding-top:176px}
.testimonial h2{font-size:30px}
.testimonial .sub{font-size:15px;margin-top:4px;opacity:.9}
.testimonial .client{width:56px;height:56px;border-radius:50%;background:#8d9aa8;margin:40px auto 8px}
.testimonial .name{font-size:12px;font-weight:700}
.testimonial .co{font-size:11px;opacity:.8}
.testimonial blockquote{width:720px;margin:18px auto 0;font-size:12px;line-height:1.6;opacity:.9}

/* benefits */
.benefits{height:340px;background:var(--grey-bg)}
.benefits .section-title{margin-top:104px}
.benefit-row{display:flex;justify-content:center;gap:40px;margin-top:44px}
.benefit{width:140px;text-align:center}
.benefit .icon{width:60px;height:60px;border-radius:50%;background:var(--blue);margin:0 auto 12px;display:flex;align-items:center;justify-content:center}
.benefit span{font-size:12px;font-weight:700;color:#333}

/* service area */
.area{height:180px}
.area .img{position:absolute;inset:0;background:linear-gradient(180deg,#56606a,#3d4a43 60%,#2c352f)}
.area .inner{position:relative;text-align:center;color:var(--white);padding-top:48px}
.area h2{font-size:28px}
.area p{font-size:12px;margin-top:8px;opacity:.9}

/* footer */
.site-footer{height:412px;background:var(--footer);color:#aab;display:flex;padding:44px 160px 0;gap:40px}
.site-footer h6{color:var(--blue);font-family:"Roboto Condensed",sans-serif;font-size:14px;text-transform:uppercase;margin-bottom:14px}
.f-col{font-size:11px;line-height:1.9}
.f-about{width:280px}
.f-about .logo{font-size:22px;margin-bottom:16px}
.f-links{width:140px}
.f-contact{width:200px}
.f-news{width:240px}
.f-news input{display:block;width:100%;height:30px;border:none;margin:10px 0 8px;padding:0 8px;font-size:11px}
.f-socials{display:flex;gap:6px;margin-top:12px}
.f-socials i{width:22px;height:22px;background:#3a3f46;display:block}
.footer-bottom{height:40px;background:var(--footer-bottom);color:#888;font-size:11px;display:flex;align-items:center;justify-content:center}
</style>
</head>
<body>

<div class="topbar">
  <div class="left"><span>✉ info@vaultlinerecords.com.au</span><span>☎ 1300 555 014</span></div>
  <div class="right"><span class="cart"><span class="cart-badge"></span></span><span style="margin-left:12px">Contact with us</span><span class="dot"></span><span class="dot"></span><span class="dot"></span></div>
</div>

<header class="site-header">
  <div class="logo"><span class="mark"></span>Vaultline Records</div>
  <nav class="nav"><span>Home</span><span>About Us ▾</span><span>Service Details ▾</span><span>Testimonial</span><span>Our Team</span><span>Contact</span><span class="phone-btn">1300 555 014</span></nav>
</header>

<section class="hero">
  <div class="hero-photo" role="img" aria-label="Courier delivering an archive box to a smiling office worker"></div>
  <div class="hero-headline">
    <h1 class="heading">Need access to your files or boxes?</h1><br>
    <p>Our friendly team are available to get your archived files to you when you need it. Fast.</p>
  </div>
  <form class="quote-form">
    <h2 class="heading">Find out how cost effective we are in storing your archive boxes</h2>
    <div class="field">Name</div>
    <div class="field">Phone no.</div>
    <div class="field">Email</div>
    <div class="field"><span>Box Type</span><span>▾</span></div>
    <div class="field"><span>Approx. Number of Boxes</span><span>▾</span></div>
    <div class="form-btns"><span class="btn">Submit</span><span class="btn">Calculate</span></div>
  </form>
</section>

<section class="offer">
  <h2 class="section-title heading">What we offer</h2>
  <div class="offer-cards">
    <div class="offer-card c1"><div class="img" role="img" aria-label="Rows of archive boxes in a secure warehouse"></div><h3 class="heading">Offsite Storage</h3><p>Store all your archives in our secure offsite warehouse.</p></div>
    <div class="offer-card c2"><div class="img" role="img" aria-label="Paper passing through a document shredder"></div><h3 class="heading">Document Shredding</h3><p>Secure destruction of documents you no longer need.</p></div>
    <div class="offer-card c3"><div class="img" role="img" aria-label="Papers being scanned to digital files"></div><h3 class="heading">Digitisation</h3><p>Turn paper records into searchable digital files.</p></div>
    <div class="offer-card c4"><div class="img" role="img" aria-label="Stacked cardboard archive boxes"></div><h3 class="heading">Archiving Supplies</h3><p>Your one stop shop for all your archiving needs. Shop Now!</p></div>
  </div>
</section>

<section class="about">
  <div class="about-text">
    <h2 class="heading">About Vaultline Records</h2>
    <p class="lead">Vaultline Records is a wholly owned Australian company.</p>
    <p>Founded a little while ago, Vaultline Records has grown to become a trusted provider of document storage and records management services across the region. We handle every box with care and keep your files safe, indexed and ready to return whenever you need them. Our team combines modern systems with friendly, personal service so your business can stay focused on its work.</p>
    <span class="btn">Shop Now</span>
  </div>
  <div class="about-photo" role="img" aria-label="Office worker smiling while using a tablet"></div>
</section>

<section class="steps">
  <h2 class="section-title heading">How it works</h2>
  <div class="step-row">
    <div class="step">
      <svg width="44" height="48" viewBox="0 0 44 48"><polygon points="22,0 44,12 44,36 22,48 0,36 0,12" fill="var(--green)"/><path d="M14 24l6 6 10-12" stroke="#fff" stroke-width="3" fill="none"/></svg>
      <h4>We deliver boxes and Barcodes</h4><p>If you need them, we get you started with all the essentials to prepare your archives.</p>
    </div>
    <div class="step">
      <svg width="44" height="48" viewBox="0 0 44 48"><polygon points="22,0 44,12 44,36 22,48 0,36 0,12" fill="var(--green)"/><rect x="13" y="16" width="18" height="16" fill="none" stroke="#fff" stroke-width="3"/></svg>
      <h4>We pick up your documents</h4><p>When your boxes are ready, let us know and we'll collect them from your door.</p>
    </div>
    <div class="step">
      <svg width="44" height="48" viewBox="0 0 44 48"><polygon points="22,0 44,12 44,36 22,48 0,36 0,12" fill="var(--green)"/><path d="M12 24h20M24 16l8 8-8 8" stroke="#fff" stroke-width="3" fill="none"/></svg>
      <h4>We Store Your Documents</h4><p>Your documents are stored in our secure, purpose built facility in Melbourne.</p>
    </div>
  </div>
</section>

<section class="team">
  <svg class="bg-shape" width="1200" height="520" viewBox="0 0 1200 520"><rect width="1200" height="520" fill="var(--blue)"/><polygon points="0,520 1200,300 1200,520" fill="var(--pink)"/></svg>
  <h2 class="section-title light heading">The Vaultline Team</h2>
  <div class="team-row">
    <div class="member"><div class="avatar" role="img" aria-label="Portrait of the director"></div><h5 class="heading">Daniel Harte</h5><div class="role">Director</div><div class="socials"><i></i><i></i><i></i></div><div class="mail">daniel@vaultlinerecords.com.au</div></div>
    <div class="member"><div class="avatar" role="img" aria-label="Portrait of the CEO"></div><h5 class="heading">Marcus Flynn</h5><div class="role">CEO</div><div class="socials"><i></i><i></i><i></i></div><div class="mail">marcus@vaultlinerecords.com.au</div></div>
    <div class="member"><div class="avatar" role="img" aria-label="Portrait of the supervisor"></div><h5 class="heading">Owen Pryce</h5><div class="role">Supervisor Head</div><div class="socials"><i></i><i></i><i></i></div><div class="mail">owen@vaultlinerecords.com.au</div></div>
    <div class="member"><div class="avatar" role="img" aria-label="Portrait of the data head"></div><h5 class="heading">Leah Corrigan</h5><div class="role">Data Head</div><div class="socials"><i></i><i></i><i></i></div><div class="mail">leah@vaultlinerecords.com.au</div></div>
  </div>
</section>

<section class="cta-strip">
  <h3 class="heading">We store your documents...smarter</h3>
  <span class="btn">Apply first for discount</span>
  <span class="btn red">Call us today</span>
</section>

<section class="testimonial">
  <div class="img" role="img" aria-label="Dim office interior with staff at work"></div>
  <div class="inner">
    <h2 class="heading">Testimonial</h2>
    <div class="sub">What our clients say about us</div>
    <div class="client" role="img" aria-label="Client portrait"></div>
    <div class="name">Nora Castwell</div>
    <div class="co">Client Company</div>
    <blockquote>Their team made moving our archives simple and stress free. Files come back quickly whenever we ask, and the staff are always friendly and helpful. We would happily recommend them to any business.</blockquote>
  </div>
</section>

<section class="benefits">
  <h2 class="section-title heading">Benefits</h2>
  <div class="benefit-row">
    <div class="benefit"><div class="icon"><svg width="28" height="28"><path d="M6 14l6 6 10-12" stroke="#fff" stroke-width="3" fill="none"/></svg></div><span>No lock-in contracts</span></div>
    <div class="benefit"><div class="icon"><svg width="28" height="28"><circle cx="14" cy="10" r="5" fill="#fff"/><rect x="6" y="17" width="16" height="8" rx="3" fill="#fff"/></svg></div><span>Expert Staff</span></div>
    <div class="benefit"><div class="icon"><svg width="28" height="28"><circle cx="14" cy="14" r="10" stroke="#fff" stroke-width="3" fill="none"/><path d="M14 8v6l4 3" stroke="#fff" stroke-width="2.5" fill="none"/></svg></div><span>Speedy Retrievals</span></div>
    <div class="benefit"><div class="icon"><svg width="28" height="28"><rect x="4" y="6" width="20" height="14" stroke="#fff" stroke-width="3" fill="none"/><path d="M10 24h8" stroke="#fff" stroke-width="3"/></svg></div><span>Simple Online Software</span></div>
    <div class="benefit"><div class="icon"><svg width="28" height="28"><path d="M8 6h12v16H8z M11 11h6M11 16h6" stroke="#fff" stroke-width="2.5" fill="none"/></svg></div><span>Competitive Pricing</span></div>
    <div class="benefit"><div class="icon"><svg width="28" height="28"><circle cx="14" cy="14" r="10" fill="none" stroke="#fff" stroke-width="3"/><path d="M9 14l4 4 7-8" stroke="#fff" stroke-width="2.5" fill="none"/></svg></div><span>Money Back Guarantee</span></div>
  </div>
</section>

<section class="area">
  <div class="img" role="img" aria-label="Aerial view over Melbourne suburbs and river"></div>
  <div class="inner">
    <h2 class="heading">We service the Melbourne area</h2>
    <p>Pick up and delivery across greater Melbourne and surrounding suburbs, on time, every time.</p>
  </div>
</section>

<footer class="site-footer">
  <div class="f-col f-about">
    <div class="logo"><span class="mark"></span>Vaultline Records</div>
    <p>We offer a range of services for storage and records management. Our friendly team are ready to help you store, retrieve and protect the files your business depends on, with simple pricing.</p>
  </div>
  <div class="f-col f-links"><h6>Links</h6>Home<br>About Us<br>Service Details<br>Testimonial<br>Our Team<br>Contact</div>
  <div class="f-col f-contact"><h6>Contact</h6>☎ 1300 555 014<br>✉ info@vaultlinerecords.com.au<br>☎ 1300 555 014<div class="f-socials"><i></i><i></i><i></i><i></i></div></div>
  <div class="f-col f-news"><h6>Newsletter</h6>Subscribe to our newsletter to receive latest updates<input type="text" placeholder="Email address"><span class="btn" style="font-size:12px;padding:7px 16px">Subscribe</span></div>
</footer>
<div class="footer-bottom">© 2024 Vaultline Records. All rights reserved.</div>

</body>
</html>
```